2020-23 Strategic Plan - Graphic Design Work

We would would like to have our strategic plan designed. It should be two pages.

- I am looking for suggestions on ways to lay this out. I don’t like this boxy layout. It was great for the committee as we went through multiple versions, but I’d prefer the final not follow this boxy format

- I’ve included a few images we own (feel free to use any or none of them). Also attached our logo.

- Have a look at our new website to see our new branding look and feel (launching next week) https://thevorlex.plinthweb.com/

- I've included a copy of our logo.

Target Market(s)

Membership

Other font styles liked:
• Lato

Requirements
Must have
• Excellent layout. Easy to ready. Consistent with branding.

```html
<!DOCTYPE html>
<html lang="en">
<head>
<meta charset="UTF-8">
<title>2020-2023 Strategic Plan – Vorlex Institute of Assessors</title>
<link href="https://fonts.googleapis.com/css2?family=Montserrat:wght@400;500;600;700;800&display=swap" rel="stylesheet">
<style>
  :root {
    --brand-dark: #0f4a26;
    --brand-green: #4b9232;
    --ink: #2b2b2b;
    --white: #ffffff;
  }
  * { margin: 0; padding: 0; box-sizing: border-box; }
  html, body { width: 1200px; height: 676px; overflow: hidden; background: var(--white); }
  body { font-family: 'Montserrat', sans-serif; color: var(--ink); }
  .page { position: relative; width: 1200px; height: 676px; overflow: hidden; }

  .sidebar { position: absolute; left: 0; top: 0; width: 374px; height: 676px; background: var(--white); }
  .brand { position: absolute; left: 64px; top: 80px; display: flex; align-items: center; gap: 10px; }
  .brand-dot { width: 34px; height: 34px; border-radius: 50%; background: var(--brand-dark); flex: none; }
  .brand-name { font-size: 15px; font-weight: 700; color: var(--brand-dark); line-height: 1.15; width: 140px; }

  .plan-title { position: absolute; left: 64px; top: 175px; font-size: 24.5px; font-weight: 800; line-height: 1.15; color: var(--brand-dark); letter-spacing: 0.2px; }
  .intro { position: absolute; left: 64px; top: 251px; width: 256px; font-size: 13.6px; line-height: 16.5px; color: var(--ink); hyphens: auto; }
  .date { position: absolute; left: 64px; top: 560px; font-size: 18.5px; font-weight: 800; color: var(--brand-green); }
  .site { position: absolute; left: 64px; top: 584px; font-size: 12.2px; font-weight: 700; color: var(--ink); }

  .hero { position: absolute; left: 374px; top: 0; width: 826px; height: 338px;
    background: radial-gradient(ellipse at 30% 45%, #e9e6e3 0%, #b9c0c8 40%, #6f7c88 75%, #4a5560 100%); }

  .band { position: absolute; left: 374px; top: 338px; width: 826px; height: 338px; background: var(--brand-green); color: var(--white); }
  .pillar { position: absolute; top: 40px; width: 185px; }
  .pillar.vision { left: 72px; }
  .pillar.mission { left: 323px; }
  .pillar.values { left: 575px; }
  .pillar-icon { width: 86px; height: 86px; border: 2px solid var(--white); border-radius: 50%; display: flex; align-items: center; justify-content: center; }
  .pillar-title { margin-top: 16px; font-size: 18.5px; font-weight: 500; }
  .pillar-text { margin-top: 10px; font-size: 11.3px; font-weight: 600; line-height: 12.5px; hyphens: auto; }
</style>
</head>
<body>
<div class="page">
  <aside class="sidebar">
    <div class="brand">
      <span class="brand-dot"></span>
      <span class="brand-name">Vorlex Institute of Assessors</span>
    </div>
    <h1 class="plan-title">2020-2023<br>STRAGETIC PLAN</h1>
    <p class="intro">With over 1,250 members, the Vorlex Institute of Assessors is Canada’s largest association of property assessment and taxation professionals. Our diverse membership is comprised of individuals from the private and public sectors practicing in the fields of assessment, consultancy, appraisal, taxation and law. Incorporated in May 1957, the VIA is dedicated to advancing the interests, education and professional competence of its members. Our members are highly qualified and widely recognized as the leading professionals in the property assessment industry.</p>
    <p class="date">JULY 2020</p>
    <p class="site">www.thevorlex.plinthweb.com</p>
  </aside>

  <div class="hero" role="img" aria-label="Photo of professionals seated in a group discussion"></div>

  <section class="band">
    <div class="pillar vision">
      <div class="pillar-icon">
        <svg width="38" height="26" viewBox="0 0 38 26" fill="#fff">
          <rect x="6" y="0" width="8" height="6" rx="2"/><rect x="24" y="0" width="8" height="6" rx="2"/>
          <rect x="15" y="8" width="8" height="6" rx="1"/>
          <circle cx="9" cy="17" r="9"/><circle cx="29" cy="17" r="9"/>
          <circle cx="9" cy="17" r="5" fill="#4b9232"/><circle cx="29" cy="17" r="5" fill="#4b9232"/>
        </svg>
      </div>
      <h2 class="pillar-title">Vision</h2>
      <p class="pillar-text">To be the industry leader in education, ethical standards, and professional accreditation in the field of property assessment in Canada.</p>
    </div>
    <div class="pillar mission">
      <div class="pillar-icon">
        <svg width="46" height="26" viewBox="0 0 46 26" fill="none" stroke="#fff" stroke-width="2">
          <line x1="18" y1="2" x2="30" y2="25"/><line x1="28" y1="2" x2="16" y2="25"/>
          <path d="M18 2 L4 6 L8 11 L2 16 L14 13 Z" fill="#fff"/>
          <path d="M28 2 L42 6 L38 11 L44 16 L32 13 Z" fill="#fff"/>
        </svg>
      </div>
      <h2 class="pillar-title">Mision</h2>
      <p class="pillar-text">To provide specialized education through a comprehensive approach to training which embraces all available technologies. To promote professional development and to ensure our members are recognized as experts in the field of property assessment and related functions.</p>
    </div>
    <div class="pillar values">
      <div class="pillar-icon">
        <svg width="30" height="40" viewBox="0 0 30 40" fill="#fff">
          <path d="M8 22 L2 34 L8 33 L11 38 L15 27 Z"/><path d="M22 22 L28 34 L22 33 L19 38 L15 27 Z"/>
          <circle cx="15" cy="14" r="13"/><circle cx="15" cy="14" r="8.5" fill="#4b9232"/>
          <path d="M15 9 L16.5 12.5 L20 12.8 L17.3 15 L18.2 18.5 L15 16.6 L11.8 18.5 L12.7 15 L10 12.8 L13.5 12.5 Z"/>
        </svg>
      </div>
      <h2 class="pillar-title">Values</h2>
      <p class="pillar-text">The Vorlex Institute of Assessors and its members value professionalism, inclusivity, diversity, integrity, ethics, accountability, and expertise. The VIA is committed to serving all members and stakeholders with competence and respect, rejecting all forms of prejudice and discrimination.</p>
    </div>
  </section>
</div>
</body>
</html>
```